TEK Logistics - Banner 2.5' x 8' for 20+ locations

Need a banner designed that will pop. This banner will be displayed at over 20 of our transportation facilities. Goal is for the banner to grab the attention of employees, contractors and clients and help reinforce our mission and core values. Designed needs to include TEK Logo, our core values and mission statement. Red and Black are the main company colors and we need to stay within that theme and color pallet. Attached is a previous version that was too basic and boring. Willing to consider a design that excludes the mission statement.

Gathering more feedback

```html
<!DOCTYPE html>
<html lang="en">
<head>
<meta charset="utf-8">
<title>TEK Logistics – Mission &amp; Core Values Banner</title>
<link href="https://fonts.googleapis.com/css2?family=Exo+2:wght@700&family=Raleway:wght@500&display=swap" rel="stylesheet">
<style>
  :root {
    --brand-red: #d7261e;
    --brand-black: #2a2a2a;
    --ink: #333333;
    --paper: #ffffff;
    --photo-warm: #b58a5a;
    --photo-dark: #3a3232;
    --photo-light: #d9cbb8;
  }
  html, body {
    margin: 0;
    padding: 0;
    overflow: hidden;
    background: var(--paper);
  }
  .banner {
    position: relative;
    width: 1200px;
    height: 375px;
    overflow: hidden;
    background: var(--paper);
    font-family: "Raleway", Arial, sans-serif;
    color: var(--ink);
  }
  .banner__art,
  .banner__photo {
    position: absolute;
    left: 0;
    top: 0;
    width: 1200px;
    height: 375px;
  }
  .brand-name {
    position: absolute;
    right: 118px;
    top: 62px;
    margin: 0;
    font-family: "Exo 2", Arial, sans-serif;
    font-weight: 700;
    font-size: 26px;
    color: var(--brand-red);
    letter-spacing: 0.5px;
  }
  .content {
    position: absolute;
    left: 508px;
    top: 144px;
    width: 620px;
  }
  .section-title {
    margin: 0;
    font-family: "Exo 2", Arial, sans-serif;
    font-weight: 700;
    font-size: 19.5px;
    line-height: 1;
    color: var(--brand-red);
  }
  .mission__text {
    margin: 8px 0 0;
    font-size: 16px;
    line-height: 23px;
  }
  .values {
    margin-top: 17px;
  }
  .values__list {
    margin: 8px 0 0;
    padding: 0;
    list-style: none;
    display: grid;
    grid-template-columns: 343px auto;
    grid-auto-flow: column;
    grid-template-rows: repeat(3, 23px);
    font-size: 16px;
    line-height: 23px;
  }
</style>
</head>
<body>
<main class="banner">
  <svg class="banner__photo" viewBox="0 0 1200 375" role="img" aria-label="Photo of a red forklift lifting a large cardboard box on a wooden pallet inside a warehouse">
    <defs>
      <linearGradient id="photoTone" x1="0" y1="0" x2="1" y2="0">
        <stop offset="0" stop-color="var(--photo-dark)"/>
        <stop offset="0.35" stop-color="#7a4a3e"/>
        <stop offset="0.7" stop-color="var(--photo-warm)"/>
        <stop offset="1" stop-color="var(--photo-light)"/>
      </linearGradient>
    </defs>
    <polygon points="0,0 505,0 330,375 0,375" fill="url(#photoTone)"/>
  </svg>

  <svg class="banner__art" viewBox="0 0 1200 375" aria-hidden="true">
    <polygon class="divider-dark" points="505,0 514,0 340,375 330,375" fill="var(--brand-black)"/>
    <polygon class="divider-red" points="514,0 522,0 350,375 340,375" fill="var(--brand-red)"/>
    <path class="swoosh-red" d="M344 322 Q418 328 446 375" fill="none" stroke="var(--brand-red)" stroke-width="9"/>
    <path class="swoosh-dark" d="M347 345 Q382 350 398 375" fill="none" stroke="var(--brand-black)" stroke-width="7"/>
    <path class="swoosh-red" d="M1200 309 Q1112 314 1080 375" fill="none" stroke="var(--brand-red)" stroke-width="13"/>
    <path class="swoosh-dark" d="M1200 331 Q1140 337 1120 375" fill="none" stroke="var(--brand-black)" stroke-width="8"/>
    <rect class="base-band" x="330" y="370" width="870" height="5" fill="var(--brand-red)"/>
  </svg>

  <p class="brand-name">TEK Logistics</p>

  <section class="content">
    <div class="mission">
      <h2 class="section-title">Mission Statement</h2>
      <p class="mission__text">Provide the best customer experience while creating an environment of growth and opportunity for our customers, employees, and service providers.</p>
    </div>
    <div class="values">
      <h2 class="section-title">Core Values</h2>
      <ul class="values__list">
        <li>Do the right things for the right reasons</li>
        <li>Pursue growth and development</li>
        <li>Build a positive team atmosphere</li>
        <li>Deliver WOW through service</li>
        <li>Do everything Safely</li>
        <li>Have Fun</li>
      </ul>
    </div>
  </section>
</main>
</body>
</html>
```